Therapy Services & Training

I provide counseling/therapy to individuals and families. I also travel the country and provide training at conferences.
I would like to see a card which takes my company name and design a logo using the letters "HWAE".
Target Market(s)
Therapists, non-profit organizations, clients looking for therapy
Industry/Entity Type
Training
Contact Information for Business Card
Harborview Wellness Advising & Education LLC
Delia Marsh, M.S.W., LCSW
Clinical Therapist & Trainer
Providing clinical therapy services to individuals, families, couples & children. We also provide life coaching and crisis training.
counselordelia@mailbrook.net
www.harborviewwellnessadvising.com
(555) 214-3092
Cedar Bend, IL 60999
(BACK SIDE OF CARD)
We are certified by the Ongoing Professional Lawyer Studies (OPLS) Council of the Prairie High Tribunal to provide Continuing Legal Education (CLE) credits to Illinois attorneys. Call about what courses we offer! (555) 214-3092

```html
<!DOCTYPE html>
<html lang="en">
<head>
<meta charset="utf-8">
<title>Harborview Wellness Advising &amp; Education — Business Card</title>
<link rel="stylesheet" href="https://fonts.googleapis.com/css2?family=Mulish:wght@300;400;600;700&display=swap">
<style>
  :root {
    --backdrop: #ecebe8;
    --card: #ffffff;
    --ink: #111111;
    --brand-blue: #2f7bc0;
    --text-blue: #3a7cc4;
    --brand-purple: #582a8e;
    --brand-lilac: #b59ac8;
  }
  * { margin: 0; padding: 0; box-sizing: border-box; }
  html, body {
    width: 1200px; height: 1000px; overflow: hidden;
    background: var(--backdrop);
    font-family: "Mulish", "Avenir", sans-serif;
  }
  .canvas { position: relative; width: 1200px; height: 1000px; }
  .card {
    position: absolute;
    background: var(--card);
    overflow: hidden;
  }
  .card--front { left: 460px; top: 123px; width: 649px; height: 379px; z-index: 2; }
  .card--back  { left: 53px;  top: 468px; width: 646px; height: 378px; z-index: 1; }

  .brand-mark {
    position: absolute;
    display: flex; align-items: center; gap: 10px;
    color: var(--brand-purple);
    font-weight: 700; font-size: 26px; letter-spacing: 2px;
  }
  .brand-mark__dot {
    width: 46px; height: 46px; border-radius: 50%;
    background: var(--brand-purple);
  }
  .card--front .brand-mark { left: 40px; top: 60px; }
  .card--back .brand-mark { right: 40px; bottom: 50px; }

  .company-name {
    position: absolute; right: 49px; top: 37px;
    text-align: right; color: var(--ink);
    font-weight: 400; font-size: 24px; line-height: 30px;
  }
  .contact {
    position: absolute; right: 48px; top: 203px;
    text-align: right; font-size: 13px; line-height: 16px;
  }
  .contact__name {
    color: var(--brand-purple); font-weight: 700;
    font-size: 30px; line-height: 36px; margin-bottom: 6px;
  }
  .contact__credentials, .contact__title {
    color: var(--ink); font-weight: 600; font-size: 12px;
  }
  .contact__line { color: var(--text-blue); font-weight: 400; }

  .services, .certification, .call-to-action {
    position: absolute; left: 32px;
    color: var(--text-blue); font-weight: 300;
    font-size: 12px; line-height: 26px;
  }
  .services { top: 240px; }
  .certification { top: 100px; line-height: 25px; }
  .call-to-action { top: 250px; }
</style>
</head>
<body>
<main class="canvas">
  <section class="card card--back" aria-label="Business card back">
    <p class="certification">
      We are certified by the Ongoing Professional Lawyer Studies (OPLS) Council<br>
      of the Prairie High Tribunal to provide<br>
      Continuing Legal Education (CLE)&nbsp; credits to Illinois attorneys.
    </p>
    <p class="call-to-action">Call about what courses we offer! (555) 214-3092</p>
    <div class="brand-mark"><span class="brand-mark__dot"></span><span>HWAE</span></div>
  </section>

  <section class="card card--front" aria-label="Business card front">
    <div class="brand-mark"><span class="brand-mark__dot"></span><span>HWAE</span></div>
    <h1 class="company-name">Harborview Wellness<br>Advising &amp; Education LLC</h1>
    <p class="services">
      Providing clinical therapy services to individuals,<br>
      families, couples, and children.<br>
      We also provide life coaching and crisis training.
    </p>
    <div class="contact">
      <h2 class="contact__name">Delia Marsh</h2>
      <p class="contact__credentials">M.S.W., LCSW</p>
      <p class="contact__title">Clinical Therapist &amp; Trainer</p>
      <p class="contact__line">counselordelia@mailbrook.net</p>
      <p class="contact__line">www.harborviewwellnessadvising.com</p>
      <p class="contact__line">(555) 214-3092</p>
      <p class="contact__line">Cedar Bend, IL 60999</p>
    </div>
  </section>
</main>
</body>
</html>
```